We are in search of a new business card design for our business. We have a Mexican Grocery Store called Tortilla Grove Market, we would like to see that some have mexican design, but we are open to any type of designs.

Phone: to be announced
Fax: to be announced

Address is:
2415 Calloway Blvd
Halverton, MD 21299

```html
<!DOCTYPE html>
<html lang="en">
<head>
<meta charset="utf-8">
<title>Tortilla Grove Market – Business Card</title>
<link rel="stylesheet" href="https://fonts.googleapis.com/css2?family=Open+Sans:wght@400;600;700&display=swap">
<style>
  :root {
    --page-bg: #e6e6e4;
    --card-bg: #f7f7f5;
    --card-edge: #c4c4c1;
    --brand-red: #8e1b17;
    --brand-green: #2f6a1f;
    --icon-red: #a8221d;
    --ink: #1c1c1c;
  }
  * { margin: 0; padding: 0; box-sizing: border-box; }
  html, body {
    width: 1200px;
    height: 970px;
    overflow: hidden;
    background: var(--page-bg);
    font-family: "Open Sans", Arial, sans-serif;
  }
  .canvas {
    position: relative;
    width: 1200px;
    height: 970px;
  }
  .business-card {
    position: absolute;
    left: 172px;
    top: 270px;
    width: 856px;
    height: 476px;
    background: var(--card-bg);
    border: 1.5px solid var(--card-edge);
    border-radius: 22px;
    box-shadow: 0 10px 30px rgba(0,0,0,0.08);
  }
  .brand-block {
    position: absolute;
    left: 47px;
    top: 135px;
    width: 380px;
    height: 200px;
    display: flex;
    align-items: center;
    justify-content: center;
    gap: 16px;
  }
  .brand-dot {
    flex: none;
    width: 40px;
    height: 40px;
    border-radius: 50%;
    background: var(--brand-green);
  }
  .brand-name {
    font-weight: 700;
    font-size: 34px;
    line-height: 1.1;
    color: var(--brand-red);
  }
  .contact-block {
    position: absolute;
    left: 480px;
    top: 112px;
    color: var(--ink);
  }
  .person-name {
    font-weight: 600;
    font-size: 25px;
    line-height: 30px;
    letter-spacing: 0.4px;
    color: var(--brand-red);
  }
  .person-title {
    font-size: 20px;
    line-height: 24px;
    color: var(--brand-green);
  }
  .address {
    margin-top: 24px;
    font-size: 19.5px;
    line-height: 25px;
  }
  .contact-list {
    margin-top: 12px;
    list-style: none;
    font-size: 19.5px;
    line-height: 26.5px;
  }
  .contact-list li {
    display: flex;
    align-items: center;
    gap: 7px;
  }
  .contact-list svg {
    width: 19px;
    height: 19px;
    fill: var(--icon-red);
    flex: none;
  }
</style>
</head>
<body>
<main class="canvas">
  <section class="business-card">
    <div class="brand-block">
      <span class="brand-dot"></span>
      <p class="brand-name">Tortilla Grove<br>Market</p>
    </div>

    <div class="contact-block">
      <p class="person-name">LUCAS R. ANDERLO</p>
      <p class="person-title">Managing Director</p>

      <p class="address">2415 Calloway Blvd<br>Halverton, MD 21299</p>

      <ul class="contact-list">
        <li>
          <svg viewBox="0 0 24 24" aria-hidden="true"><path d="M3 9c0-2 4-4 9-4s9 2 9 4v1.5h-4.5V8.5h-9v2H3z"/><path d="M6 12h12l2 7H4z"/></svg>
          + 000 000 0000
        </li>
        <li>
          <svg viewBox="0 0 24 24" aria-hidden="true"><rect x="7" y="3" width="10" height="5"/><path d="M3 9h18v8h-3v-3H6v3H3z"/><rect x="7" y="15" width="10" height="6"/></svg>
          + 000 000 0000
        </li>
        <li>
          <svg viewBox="0 0 24 24" aria-hidden="true"><path d="M2 6h20v1l-10 6L2 7z"/><path d="M2 9l10 6 10-6v9H2z"/></svg>
          info@tortillagrovemarket.com
        </li>
        <li>
          <svg viewBox="0 0 24 24" aria-hidden="true"><path d="M12 2a10 10 0 1 0 0 20 10 10 0 0 0 0-20zm0 3a7 7 0 0 1 6.9 6H14l-2 2-2-2-1-4 3-2zM5.1 13h3.4l2.5 3v3.9A7 7 0 0 1 5.1 13z"/></svg>
          www.tortillagrovemarket.com
        </li>
      </ul>
    </div>
  </section>
</main>
</body>
</html>
```